Business Cards for an 'affordable luxury' inner city home builder in Calgary.

We need a business card design that emulates the progressive, innovative, culture of our company and the modern style of our homes. Use our website www.velmarcrest-ab.com as a reference for the product we build.

Our company builds homes in the inner city space of Calgary, Alberta. We build affordable luxury.

Target Market(s)

Young professional Families

Contact Information for Business Card

Try to maintain consistency with the logo font and the card font.

Requirements
Must have
• The details must include: Name, education, title, phone number, website and email (Address is not as important)
• The design must be uniques (like our logo), elegant, sophisticated and modern.

```html
<!DOCTYPE html>
<html lang="en">
<head>
<meta charset="utf-8">
<title>Velmarcrest Custom Homes – Business Cards</title>
<link href="https://fonts.googleapis.com/css2?family=Montserrat:wght@400;500;600;700&display=swap" rel="stylesheet">
<style>
  :root{
    --stage:#2b2b2b;
    --card-dark:#1e1e1e;
    --card-light:#ffffff;
    --ink:#1a1a1a;
    --ink-soft:#3c3c3c;
    --gloss:#8e8e8e;
    --white:#ffffff;
  }
  *{box-sizing:border-box;margin:0;padding:0}
  html,body{width:1200px;height:895px;overflow:hidden}
  body{background:var(--stage);font-family:"Montserrat",sans-serif;position:relative}

  .card{position:absolute;width:620px;height:354px;box-shadow:0 18px 40px rgba(0,0,0,.45)}

  /* back side */
  .card-back{left:70px;top:90px;background:var(--card-dark);display:flex;align-items:center;padding-left:150px}
  .brand-mark{width:70px;height:70px;border:3px solid #111;margin-right:28px;flex:none}
  .brand-name{color:var(--gloss);font-weight:500;font-size:32px;line-height:1.0;letter-spacing:.5px;text-transform:uppercase}

  /* front side */
  .card-front{left:510px;top:470px;background:var(--card-dark);display:flex}
  .front-info{width:330px;height:100%;background:var(--card-light);padding:34px 0 0 40px;color:var(--ink)}
  .front-brand{display:flex;align-items:center;gap:10px;font-weight:600;font-size:15px;letter-spacing:1px;text-transform:uppercase}
  .front-brand .square{width:14px;height:14px;background:var(--ink)}
  .person-name{margin-top:62px;font-weight:700;font-size:19px;letter-spacing:.4px;text-transform:uppercase}
  .person-meta{margin-top:4px;font-size:12.5px;line-height:1.35;color:var(--ink-soft)}
  .contacts{list-style:none;margin-top:14px}
  .contacts li{display:flex;align-items:center;gap:10px;font-size:12.5px;line-height:1.6;color:var(--ink-soft)}
  .contacts svg{width:13px;height:13px;flex:none}
  .front-brand-side{flex:1;display:flex;align-items:center;padding-left:40px}
  .front-brand-side .brand-name{color:var(--white);font-size:22px}
</style>
</head>
<body>
  <section class="card card-back">
    <span class="brand-mark"></span>
    <p class="brand-name">Velmarcrest<br>Custom<br>Homes Ltd</p>
  </section>

  <section class="card card-front">
    <div class="front-info">
      <div class="front-brand"><span class="square"></span>Velmarcrest</div>
      <h1 class="person-name">Adrian Kovell</h1>
      <p class="person-meta">M.Sc. in Architecture<br>Founder &amp; CEO</p>
      <ul class="contacts">
        <li>
          <svg viewBox="0 0 14 14" fill="none" stroke="#1a1a1a" stroke-width="1.4"><rect x="3.5" y="1" width="7" height="12" rx="1.2"/><line x1="6" y1="11" x2="8" y2="11"/></svg>
          403-555-0148
        </li>
        <li>
          <svg viewBox="0 0 14 14"><rect x="1" y="3" width="12" height="8" fill="#1a1a1a"/><polyline points="1,3 7,8 13,3" fill="none" stroke="#fff" stroke-width="1"/></svg>
          projects@velmarcrest-ab.com
        </li>
        <li>
          <svg viewBox="0 0 14 14" fill="none" stroke="#1a1a1a" stroke-width="1.5"><circle cx="8" cy="6" r="4"/><line x1="5" y1="9" x2="1.5" y2="12.5"/></svg>
          www.velmarcrest-ab.com
        </li>
      </ul>
    </div>
    <div class="front-brand-side">
      <p class="brand-name">Velmarcrest<br>Custom<br>Homes Ltd</p>
    </div>
  </section>
</body>
</html>
```